Envelope Design - Winner can do follow-up business

- Marvuno.com is a Swiss-based online store selling business shirts and accessories for business men
- Please visit the webpage to make yourself familiar with the company. Although the text is in German, with Google translator you should be able to understand the main content.
- Our clients are mainly business men between 30 and 60 years old. Mostly with a high income working in the service industry (banking, insurance, lawyers, etc.). Sometimes there wives purchase the shirts for them ;-)
- The colors and the logo are given, as they are also used for the print materials (please see files in attachment)
- I am running several businesses and often need a talented web designer --> the winner gets substantial follow-up business
your task:
-for our company we need a new envelope design
-It should be simple and modern
-please use one of the logos in the followings.
-suprise me :)

```html
<!DOCTYPE html>
<html lang="de">
<head>
<meta charset="utf-8">
<title>Marvuno – Envelope design proposals</title>
<link rel="stylesheet" href="https://fonts.googleapis.com/css2?family=Cinzel:wght@400;600&family=PT+Sans&display=swap">
<style>
  :root {
    --paper: #ffffff;
    --frame: #1a1a1a;
    --gold: #e3cb55;
    --gold-deep: #e6d163;
    --gold-pale: #f3eab8;
    --gold-wash: #faf5dc;
    --red: #e03a3a;
    --label: #111111;
  }
  html, body {
    margin: 0;
    padding: 0;
    width: 1200px;
    height: 1129px;
    overflow: hidden;
    background: var(--paper);
  }
  .sheet {
    position: relative;
    width: 1200px;
    height: 1129px;
  }
  .proposal-label {
    position: absolute;
    left: 40px;
    margin: 0;
    font: 400 15px/1 "PT Sans", Arial, sans-serif;
    color: var(--label);
  }
  .envelope {
    position: absolute;
    left: 232px;
    width: 736px;
    height: 319px;
    display: block;
  }
  .envelope-frame { fill: none; stroke: var(--frame); stroke-width: 1.2; }
  .brand-name {
    font-family: "Cinzel", "Times New Roman", serif;
    font-weight: 600;
    font-size: 31px;
    letter-spacing: 1px;
    fill: var(--gold);
  }
  .sender-address {
    font-family: "Cinzel", "Times New Roman", serif;
    font-weight: 400;
    font-size: 14px;
    letter-spacing: 0.5px;
    fill: var(--gold);
  }
  .sender-address--red { fill: var(--red); }
  .brand-dot { fill: var(--red); }
  .ring { fill: none; stroke: var(--gold-pale); stroke-width: 3; }
  .pale-field { fill: var(--gold-pale); opacity: 0.55; }
  .wash-field { fill: var(--gold-wash); }
</style>
</head>
<body>
<main class="sheet">

  <!-- Proposal A -->
  <p class="proposal-label" style="top:222px">Design proposal A</p>
  <svg class="envelope" style="top:53px" viewBox="0 0 736 319">
    <defs>
      <linearGradient id="band-fade" x1="0" x2="1" y1="0" y2="0">
        <stop offset="0" stop-color="var(--gold-deep)"/>
        <stop offset="0.6" stop-color="#f6edc4"/>
        <stop offset="1" stop-color="#ffffff"/>
      </linearGradient>
    </defs>
    <rect x="0" y="0" width="374" height="72" fill="url(#band-fade)" role="img" aria-label="Gold decorative band with brand motif"/>
    <rect x="0" y="249" width="374" height="70" fill="url(#band-fade)" role="img" aria-label="Gold decorative band with brand motif"/>
    <rect class="brand-dot" x="155" y="101" width="12" height="12"/>
    <text class="brand-name" x="161" y="164" text-anchor="middle">MARVUNO</text>
    <text class="sender-address" text-anchor="middle">
      <tspan x="161" y="201">Marvuno GmbH</tspan>
      <tspan x="161" y="218">Lindenweg 27</tspan>
      <tspan x="161" y="235">CH-8805 Seewil</tspan>
    </text>
    <rect class="envelope-frame" x="0.6" y="0.6" width="734.8" height="317.8"/>
  </svg>

  <!-- Proposal B -->
  <p class="proposal-label" style="top:547px">Design proposal B</p>
  <svg class="envelope" style="top:401px" viewBox="0 0 736 319">
    <defs><clipPath id="clip-b"><rect width="736" height="319"/></clipPath></defs>
    <g clip-path="url(#clip-b)">
      <circle class="ring" cx="187" cy="147" r="190"/>
      <rect class="pale-field" x="50" y="28" width="250" height="280" role="img" aria-label="Faint outline of the brand motif"/>
    </g>
    <rect class="brand-dot" x="170" y="32" width="12" height="12"/>
    <text class="brand-name" x="176" y="107" text-anchor="middle">MARVUNO</text>
    <text class="sender-address" text-anchor="middle">
      <tspan x="172" y="261">Marvuno GmbH</tspan>
      <tspan x="172" y="278">Lindenweg 27</tspan>
      <tspan x="172" y="295">CH-8805 Seewil</tspan>
    </text>
    <rect class="envelope-frame" x="0.6" y="0.6" width="734.8" height="317.8"/>
  </svg>

  <!-- Proposal C -->
  <p class="proposal-label" style="top:900px">Design proposal C</p>
  <svg class="envelope" style="top:754px" viewBox="0 0 736 319">
    <defs><clipPath id="clip-c"><rect width="736" height="319"/></clipPath></defs>
    <g clip-path="url(#clip-c)" role="img" aria-label="Large pale brand motif in soft gold">
      <circle class="wash-field" cx="205" cy="140" r="206"/>
      <rect class="wash-field" x="0" y="16" width="314" height="303"/>
    </g>
    <rect class="brand-dot" x="148" y="44" width="12" height="12"/>
    <text class="brand-name" x="154" y="119" text-anchor="middle">MARVUNO</text>
    <text class="sender-address sender-address--red" text-anchor="middle">
      <tspan x="155" y="239">Marvuno GmbH</tspan>
      <tspan x="155" y="256">Lindenweg 27</tspan>
      <tspan x="155" y="273">CH-8805 Seewil</tspan>
    </text>
    <rect class="envelope-frame" x="0.6" y="0.6" width="734.8" height="317.8"/>
  </svg>

</main>
</body>
</html>
```